Tri-fold brochue, business card, and stationary design.

Tri-fold brochure: We are looking to get a tri-fold brochure template created so we can add our content on each side of the brochure and then leave these with prospective clients during sales calls.Business card: We would like the business card to have employee name, phone number, and email address on the card. We are open to rounded corners as well.We just redid our website and we'd like all designs to be complementary to our new "Look and feel" of our website.

Contact Information for Business Card

We would like the business card to have employee name, phone number, and email address on the card. We are open to rounded corners as well.

We just redid our website and we'd like all designs to be complementary to our new "Look and feel" of our website.

```html
<!DOCTYPE html>
<html lang="en">
<head>
<meta charset="utf-8">
<title>Tealpoint Networks – Business Card Set</title>
<link href="https://fonts.googleapis.com/css2?family=Raleway:wght@400;600;700&display=swap" rel="stylesheet">
<style>
  :root{
    --sheet:#606060;
    --white:#ffffff;
    --paper-tint:#f3f4f5;
    --blue:#31a5da;
    --blue-deep:#1c86c4;
    --blue-band:#1673aa;
    --green:#a8c43a;
    --green-light:#b4d24d;
    --green-band:#7f9a31;
    --grey-logo:#e4e4e4;
  }
  *{margin:0;padding:0;box-sizing:border-box}
  html,body{width:848px;height:1200px;overflow:hidden;background:var(--sheet)}
  body{position:relative;font-family:"Raleway",sans-serif}

  .card{position:absolute;width:344px;height:222px;overflow:hidden}
  .card-front{left:62px;background:linear-gradient(160deg,var(--paper-tint) 0%,var(--white) 45%,var(--white) 70%,var(--paper-tint) 100%)}
  .card-back{left:443px}
  .row-1{top:62px}.row-2{top:342px}.row-3{top:626px}.row-4{top:904px}

  .card-art{position:absolute;inset:0;width:344px;height:222px}

  /* brand wordmark */
  .brand-dot{position:absolute;border-radius:50%}
  .brand-name{position:absolute;font-weight:700;line-height:1;white-space:nowrap}
  .card-front .brand-dot{left:78px;top:86px;width:50px;height:50px;background:var(--blue)}
  .card-front .brand-name{left:150px;top:92px;font-size:25px;color:var(--blue)}
  .card-front .brand-name small{display:block;font-size:10px;letter-spacing:7.6px;margin-top:3px}
  .card-back .brand-dot{left:47px;top:72px;width:34px;height:34px}
  .card-back .brand-name{left:64px;top:116px;transform:translateX(-50%);font-size:17px;text-align:center}
  .card-back .brand-name small{display:block;font-size:7px;letter-spacing:5px;margin-top:2px}

  /* contact block */
  .contact{position:absolute;inset:0}
  .employee-name{position:absolute;left:183px;top:52px;font-size:14px;font-weight:700}
  .job-title{position:absolute;left:184px;top:72px;font-size:10px}
  .contact-line{position:absolute;font-size:9.5px;white-space:nowrap}
  .line-phone{left:179px;top:104px}
  .line-mail{left:176px;top:125px}
  .line-web{left:174px;top:148px}
  .card-green-white .contact-line{font-weight:600}

  /* colour schemes */
  .card-green-white{--left:var(--white);--right:var(--green);--tab:var(--blue);--band:var(--blue-band);--ink:var(--white);--logo:var(--blue);--logo-dot:var(--blue)}
  .card-blue-white{--left:var(--blue);--right:var(--white);--tab:var(--green-light);--band:var(--green-band);--ink:var(--blue);--logo:var(--white);--logo-dot:var(--grey-logo)}
  .card-white-blue{--left:var(--white);--right:var(--blue);--tab:var(--green-light);--band:var(--green-band);--ink:var(--white);--logo:var(--blue);--logo-dot:var(--blue)}
  .card-green-blue{--left:var(--green-light);--right:var(--blue);--tab:var(--blue-deep);--band:var(--blue-band);--ink:var(--white);--logo:var(--white);--logo-dot:var(--white)}

  .card-back{background:var(--left)}
  .card-back .brand-name{color:var(--logo)}
  .card-back .brand-dot{background:var(--logo-dot)}
  .contact{color:var(--ink)}
  .panel-right{fill:var(--right)}
  .tab{fill:var(--tab)}
  .tab-band{fill:var(--band)}
  .icon{fill:var(--white)}
  .icon-line{fill:none;stroke:var(--white);stroke-width:1.1}
</style>
</head>
<body>

<!-- Fronts -->
<section class="card card-front row-1"><span class="brand-dot"></span><p class="brand-name">Tealpoint<small>Networks</small></p></section>
<section class="card card-front row-2"><span class="brand-dot"></span><p class="brand-name">Tealpoint<small>Networks</small></p></section>
<section class="card card-front row-3"><span class="brand-dot"></span><p class="brand-name">Tealpoint<small>Networks</small></p></section>
<section class="card card-front row-4"><span class="brand-dot"></span><p class="brand-name">Tealpoint<small>Networks</small></p></section>

<!-- Backs -->
<section class="card card-back row-1 card-green-white">
  <svg class="card-art" viewBox="0 0 344 222" aria-hidden="true">
    <polygon class="panel-right" points="147,0 344,0 344,222 121,222"/>
    <path class="tab" d="M141,40 L163,40 Q174,40 173,52 L159,185 Q158,196 147,196 L121,196 Z"/>
    <polygon class="tab-band" points="132,102 166,102 164,118 130,118"/>
    <polygon class="tab-band" points="129,123 164,123 162,139 127,139"/>
    <polygon class="tab-band" points="126,146 161,146 159,162 124,162"/>
    <circle class="icon" cx="150" cy="64" r="4"/><path class="icon" d="M143,78 Q143,69 150,69 Q157,69 157,78 Z"/>
    <path class="icon" d="M145,106 q2,-1 3,1 l-1,2 q1,3 4,4 l2,-1 q2,1 1,3 q-2,2 -5,0 q-4,-3 -5,-6 q-1,-2 1,-3z"/>
    <rect class="icon-line" x="140.5" y="127.5" width="9" height="7"/><path class="icon-line" d="M140.5,127.5 L145,131.5 L149.5,127.5"/>
    <circle class="icon-line" cx="142" cy="154" r="4.5"/><path class="icon-line" d="M137.5,154 H146.5 M142,149.5 V158.5"/>
  </svg>
  <span class="brand-dot"></span><p class="brand-name">Tealpoint<small>Networks</small></p>
  <div class="contact">
    <p class="employee-name">Employee Name</p><p class="job-title">job title</p>
    <p class="contact-line line-phone">555-014-2290</p>
    <p class="contact-line line-mail">sales@tealpointnetworks.com</p>
    <p class="contact-line line-web">www.tealpointnetworks.com</p>
  </div>
</section>

<section class="card card-back row-2 card-blue-white">
  <svg class="card-art" viewBox="0 0 344 222" aria-hidden="true">
    <polygon class="panel-right" points="147,0 344,0 344,222 121,222"/>
    <path class="tab" d="M141,40 L163,40 Q174,40 173,52 L159,185 Q158,196 147,196 L121,196 Z"/>
    <polygon class="tab-band" points="132,102 166,102 164,118 130,118"/>
    <polygon class="tab-band" points="129,123 164,123 162,139 127,139"/>
    <polygon class="tab-band" points="126,146 161,146 159,162 124,162"/>
    <circle class="icon" cx="150" cy="64" r="4"/><path class="icon" d="M143,78 Q143,69 150,69 Q157,69 157,78 Z"/>
    <path class="icon" d="M145,106 q2,-1 3,1 l-1,2 q1,3 4,4 l2,-1 q2,1 1,3 q-2,2 -5,0 q-4,-3 -5,-6 q-1,-2 1,-3z"/>
    <rect class="icon-line" x="140.5" y="127.5" width="9" height="7"/><path class="icon-line" d="M140.5,127.5 L145,131.5 L149.5,127.5"/>
    <circle class="icon-line" cx="142" cy="154" r="4.5"/><path class="icon-line" d="M137.5,154 H146.5 M142,149.5 V158.5"/>
  </svg>
  <span class="brand-dot"></span><p class="brand-name">Tealpoint<small>Networks</small></p>
  <div class="contact">
    <p class="employee-name">Employee Name</p><p class="job-title">job title</p>
    <p class="contact-line line-phone">555-014-2290</p>
    <p class="contact-line line-mail">sales@tealpointnetworks.com</p>
    <p class="contact-line line-web">www.tealpointnetworks.com</p>
  </div>
</section>

<section class="card card-back row-3 card-white-blue">
  <svg class="card-art" viewBox="0 0 344 222" aria-hidden="true">
    <polygon class="panel-right" points="147,0 344,0 344,222 121,222"/>
    <path class="tab" d="M141,40 L163,40 Q174,40 173,52 L159,185 Q158,196 147,196 L121,196 Z"/>
    <polygon class="tab-band" points="132,102 166,102 164,118 130,118"/>
    <polygon class="tab-band" points="129,123 164,123 162,139 127,139"/>
    <polygon class="tab-band" points="126,146 161,146 159,162 124,162"/>
    <circle class="icon" cx="150" cy="64" r="4"/><path class="icon" d="M143,78 Q143,69 150,69 Q157,69 157,78 Z"/>
    <path class="icon" d="M145,106 q2,-1 3,1 l-1,2 q1,3 4,4 l2,-1 q2,1 1,3 q-2,2 -5,0 q-4,-3 -5,-6 q-1,-2 1,-3z"/>
    <rect class="icon-line" x="140.5" y="127.5" width="9" height="7"/><path class="icon-line" d="M140.5,127.5 L145,131.5 L149.5,127.5"/>
    <circle class="icon-line" cx="142" cy="154" r="4.5"/><path class="icon-line" d="M137.5,154 H146.5 M142,149.5 V158.5"/>
  </svg>
  <span class="brand-dot"></span><p class="brand-name">Tealpoint<small>Networks</small></p>
  <div class="contact">
    <p class="employee-name">Employee Name</p><p class="job-title">job title</p>
    <p class="contact-line line-phone">555-014-2290</p>
    <p class="contact-line line-mail">sales@tealpointnetworks.com</p>
    <p class="contact-line line-web">www.tealpointnetworks.com</p>
  </div>
</section>

<section class="card card-back row-4 card-green-blue">
  <svg class="card-art" viewBox="0 0 344 222" aria-hidden="true">
    <polygon class="panel-right" points="147,0 344,0 344,222 121,222"/>
    <path class="tab" d="M141,40 L163,40 Q174,40 173,52 L159,185 Q158,196 147,196 L121,196 Z"/>
    <polygon class="tab-band" points="132,102 166,102 164,118 130,118"/>
    <polygon class="tab-band" points="129,123 164,123 162,139 127,139"/>
    <polygon class="tab-band" points="126,146 161,146 159,162 124,162"/>
    <circle class="icon" cx="150" cy="64" r="4"/><path class="icon" d="M143,78 Q143,69 150,69 Q157,69 157,78 Z"/>
    <path class="icon" d="M145,106 q2,-1 3,1 l-1,2 q1,3 4,4 l2,-1 q2,1 1,3 q-2,2 -5,0 q-4,-3 -5,-6 q-1,-2 1,-3z"/>
    <rect class="icon-line" x="140.5" y="127.5" width="9" height="7"/><path class="icon-line" d="M140.5,127.5 L145,131.5 L149.5,127.5"/>
    <circle class="icon-line" cx="142" cy="154" r="4.5"/><path class="icon-line" d="M137.5,154 H146.5 M142,149.5 V158.5"/>
  </svg>
  <span class="brand-dot"></span><p class="brand-name">Tealpoint<small>Networks</small></p>
  <div class="contact">
    <p class="employee-name">Employee Name</p><p class="job-title">job title</p>
    <p class="contact-line line-phone">555-014-2290</p>
    <p class="contact-line line-mail">sales@tealpointnetworks.com</p>
    <p class="contact-line line-web">www.tealpointnetworks.com</p>
  </div>
</section>

</body>
</html>
```